Brightvantage.com tech company website

Current site is www.brightvantage.com. The site will tell you about our company.

Designs we like are:
http://hugeinfo.quellport.com
www.zolbar.com
www.fendrossa.com

Target Market(s)

B2B

Industry/Entity Type

It Company

Coding

Coded - Design and coding required

Number of Pages Required

5+ page

Requirements
Must have
• We want to entice without giving away too much info. We like graphics and colors. But website must look official and credible.

```html
<!DOCTYPE html>
<html lang="en">
<head>
<meta charset="utf-8">
<title>Brightvantage — Big Data and Analytics</title>
<link href="https://fonts.googleapis.com/css2?family=Oswald:wght@300;400;500;600&family=Open+Sans:wght@400;600;700&display=swap" rel="stylesheet">
<style>
:root{
  --navy:#0c1b33;
  --navy-deep:#081326;
  --blue:#1f7fd1;
  --blue-dark:#155fa3;
  --ink:#2b2f36;
  --muted:#7a818b;
  --line:#e3e6ea;
  --paper:#ffffff;
  --soft:#f4f6f8;
  --topbar-text:#c9d2de;
}
*{box-sizing:border-box;margin:0;padding:0}
html,body{width:1200px;height:3868px;overflow:hidden}
body{font-family:"Open Sans",Arial,sans-serif;color:var(--ink);background:var(--paper);font-size:13px;line-height:1.6}
.wrap{width:1080px;margin:0 auto;position:relative}
h2.section-title{font-family:"Oswald",Arial,sans-serif;font-weight:400;font-size:40px;text-align:center;color:var(--ink);letter-spacing:.5px}
h2.section-title span{color:var(--blue)}
.title-rule{width:70px;height:3px;background:var(--blue);margin:12px auto 22px}
.lead{text-align:center;color:var(--muted);font-size:13px;width:820px;margin:0 auto}

/* top bar */
.topbar{height:32px;background:var(--navy-deep);color:var(--topbar-text);font-size:12px}
.topbar .wrap{display:flex;justify-content:space-between;align-items:center;height:32px}
.topbar .contact-line{display:flex;gap:22px}
.topbar .social{display:flex;gap:10px}
.topbar .social i{display:block;width:10px;height:10px;border-radius:50%;background:#8592a6}

/* header */
.site-header{height:100px;background:var(--paper);border-bottom:1px solid var(--line)}
.site-header .wrap{display:flex;justify-content:space-between;align-items:center;height:100px}
.brand{display:flex;align-items:center;gap:12px;font-family:"Oswald",Arial,sans-serif;font-weight:500;font-size:30px;color:var(--navy);letter-spacing:1px}
.brand i{width:26px;height:26px;background:var(--blue);display:block}
.main-nav{display:flex;gap:30px;font-family:"Oswald",Arial,sans-serif;font-size:15px;text-transform:uppercase;color:var(--ink)}
.main-nav .active{color:var(--blue)}

/* hero */
.hero{height:440px;position:relative;background:linear-gradient(135deg,#0a1d3d 0%,#17407a 45%,#0e2a55 75%,#0a1a33 100%);color:#fff;text-align:center}
.hero .backdrop{position:absolute;inset:0;background:radial-gradient(circle at 75% 30%,rgba(90,160,230,.35),transparent 45%),radial-gradient(circle at 20% 70%,rgba(60,120,200,.25),transparent 40%)}
.hero .content{position:relative;padding-top:78px}
.hero .kicker{font-family:"Oswald",Arial,sans-serif;font-weight:300;font-size:40px}
.hero h1{font-family:"Oswald",Arial,sans-serif;font-weight:500;font-size:64px;line-height:1.1;letter-spacing:1px;margin-top:4px}
.hero .tagline{font-family:"Oswald",Arial,sans-serif;font-size:22px;margin-top:36px;color:#dbe6f5}
.cities{display:flex;justify-content:center;gap:14px;margin-top:26px}
.cities span{background:var(--blue);padding:10px 22px;font-size:14px;font-weight:600}

/* about */
.about{height:918px;padding-top:98px}
.features{display:grid;grid-template-columns:repeat(4,1fr);margin-top:40px;border-top:1px solid var(--line);border-left:1px solid var(--line)}
.feature{height:268px;padding:30px 26px;border-right:1px solid var(--line);border-bottom:1px solid var(--line)}
.features .gap{grid-column:1/-1;height:40px;border-right:none;border-left:none;background:var(--paper);margin-left:-1px}
.feature svg{width:42px;height:42px;display:block;margin-bottom:14px}
.feature h3{font-family:"Oswald",Arial,sans-serif;font-weight:400;font-size:15px;text-transform:uppercase;color:var(--ink);line-height:1.35;margin-bottom:10px;min-height:40px}
.feature p{color:var(--muted);font-size:12px}

/* news */
.news{height:610px;padding-top:20px}
.lead .accent{color:var(--blue);font-weight:700}
.cards{display:grid;grid-template-columns:repeat(3,1fr);gap:30px;margin-top:38px}
.card{background:var(--soft)}
.card .photo{height:180px}
.card .body{padding:18px 20px;height:180px}
.card h4{font-family:"Oswald",Arial,sans-serif;font-weight:400;font-size:18px;color:var(--ink)}
.card .meta{font-size:11px;color:var(--blue);margin:4px 0 10px}
.card p{font-size:12px;color:var(--muted)}

/* clients */
.clients{height:200px;padding-top:30px}

/* testimonial */
.testimonial{height:370px;background:linear-gradient(120deg,#15181d,#2a2f36 55%,#14171b);color:#d7dbe0;text-align:center;padding-top:60px}
.avatar{width:96px;height:96px;border-radius:50%;background:#7d8794;border:4px solid #fff;margin:0 auto 22px}
.testimonial blockquote{font-style:italic;font-size:15px;width:680px;margin:0 auto}
.testimonial .name{font-family:"Oswald",Arial,sans-serif;color:var(--blue);font-size:20px;margin-top:18px}
.testimonial .role{font-size:12px;color:#9aa2ad}

/* contact */
.contact{height:700px;padding-top:82px}
.contact .lead strong{color:var(--blue)}
.contact-grid{display:grid;grid-template-columns:1fr 1fr;gap:60px;margin-top:58px}
.contact h3{font-family:"Oswald",Arial,sans-serif;font-weight:400;font-size:24px;margin-bottom:18px}
.info-list{list-style:none}
.info-list li{display:flex;align-items:center;gap:12px;margin-bottom:14px;color:var(--muted)}
.info-list i{width:22px;height:22px;border-radius:50%;background:var(--blue);display:block;flex:none}
.field{border:1px solid #cfd4da;height:38px;margin-bottom:12px;padding:9px 12px;color:#9aa1aa;font-size:12px}
.field.message{height:92px}
.submit{display:inline-block;background:var(--navy);color:#fff;padding:9px 26px;font-size:13px}

/* map */
.map{height:270px;background:linear-gradient(160deg,#e8ebe3,#d7e2d0 40%,#e4e6df 70%,#cfdbe6)}

/* footer */
.site-footer{height:228px;background:var(--navy);text-align:center;padding-top:62px;color:#8593a8;font-size:12px}
.site-footer .social{display:flex;justify-content:center;gap:16px;margin-bottom:50px}
.site-footer .social i{width:44px;height:44px;border-radius:50%;background:#1b2b47;display:block}
</style>
</head>
<body>

<div class="topbar">
  <div class="wrap">
    <div class="contact-line"><span>info@brightvantage.com</span><span>+1 (555) 014-2290</span></div>
    <div class="social"><i></i><i></i><i></i><i></i><i></i></div>
  </div>
</div>

<header class="site-header">
  <div class="wrap">
    <div class="brand"><i></i>BRIGHTVANTAGE</div>
    <nav class="main-nav">
      <span>Home</span><span>About</span><span class="active">Big Data and Analytics</span><span>Perception and Influence</span><span>Case Studies</span><span>Contact</span>
    </nav>
  </div>
</header>

<section class="hero">
  <div class="backdrop" role="img" aria-label="Dark blue data dashboard backdrop with charts and graphs"></div>
  <div class="content">
    <div class="kicker">Unlock the Value of Your Data</div>
    <h1>BIG DATA AND ANALYTICS</h1>
    <div class="tagline">Your IT Infrastructure Matters.</div>
    <div class="cities"><span>Ashford</span><span>Marlow Bay</span><span>Kessington</span><span>Dunmere</span></div>
  </div>
</section>

<section class="about">
  <div class="wrap">
    <h2 class="section-title">About <span>BIG DATA AND ANALYTICS</span></h2>
    <div class="title-rule"></div>
    <p class="lead">Brightvantage is expert at data collection and analysis, extracting the data important to business, and putting it into a format most useful to the client. The following is a partial list of our capabilities in this area. For more detailed information, contact us at info@brightvantage.com.</p>

    <div class="features">
      <div class="feature">
        <svg viewBox="0 0 42 42"><circle cx="21" cy="12" r="7" fill="#1f7fd1"/><rect x="8" y="24" width="26" height="14" rx="3" fill="#1f7fd1"/></svg>
        <h3>Precision Audience Marketing</h3>
        <p>Lorem ipsum is simply dummy text of the printing and typesetting industry. Lorem Ipsum has been the industry's standard dummy text ever since the 1500s, unknown printer.</p>
      </div>
      <div class="feature">
        <svg viewBox="0 0 42 42"><circle cx="14" cy="14" r="6" fill="#1f7fd1"/><circle cx="28" cy="14" r="6" fill="#1f7fd1"/><rect x="6" y="24" width="30" height="12" rx="3" fill="#1f7fd1"/></svg>
        <h3>Lead Generation</h3>
        <p>Lorem ipsum is simply dummy text of the printing and typesetting industry. Lorem Ipsum has been the industry's standard dummy text ever since the 1500s, unknown printer.</p>
      </div>
      <div class="feature">
        <svg viewBox="0 0 42 42"><rect x="6" y="22" width="7" height="14" fill="#1f7fd1"/><rect x="17" y="14" width="7" height="22" fill="#1f7fd1"/><rect x="28" y="6" width="7" height="30" fill="#1f7fd1"/></svg>
        <h3>Data Enhancement</h3>
        <p>Lorem ipsum is simply dummy text of the printing and typesetting industry. Lorem Ipsum has been the industry's standard dummy text ever since the 1500s, unknown printer.</p>
      </div>
      <div class="feature">
        <svg viewBox="0 0 42 42"><rect x="6" y="8" width="30" height="20" rx="2" fill="none" stroke="#1f7fd1" stroke-width="4"/><rect x="14" y="32" width="14" height="4" fill="#1f7fd1"/></svg>
        <h3>Data Monetization</h3>
        <p>Lorem ipsum is simply dummy text of the printing and typesetting industry. Lorem Ipsum has been the industry's standard dummy text ever since the 1500s, unknown printer.</p>
      </div>
      <div class="feature gap"></div>
      <div class="feature">
        <svg viewBox="0 0 42 42"><circle cx="21" cy="21" r="14" fill="none" stroke="#1f7fd1" stroke-width="4"/><circle cx="21" cy="21" r="5" fill="#1f7fd1"/></svg>
        <h3>Influencer Identification and Targeting</h3>
        <p>Lorem ipsum is simply dummy text of the printing and typesetting industry. Lorem Ipsum has been the industry's standard dummy text ever since the 1500s, unknown printer.</p>
      </div>
      <div class="feature">
        <svg viewBox="0 0 42 42"><circle cx="18" cy="18" r="11" fill="none" stroke="#1f7fd1" stroke-width="4"/><path d="M26 26l10 10" stroke="#1f7fd1" stroke-width="5" stroke-linecap="round"/></svg>
        <h3>Business Intelligence</h3>
        <p>Lorem ipsum is simply dummy text of the printing and typesetting industry. Lorem Ipsum has been the industry's standard dummy text ever since the 1500s, unknown printer.</p>
      </div>
      <div class="feature">
        <svg viewBox="0 0 42 42"><path d="M6 34l10-12 8 6 12-18" fill="none" stroke="#1f7fd1" stroke-width="4" stroke-linejoin="round"/></svg>
        <h3>Competitive Advantage</h3>
        <p>Lorem ipsum is simply dummy text of the printing and typesetting industry. Lorem Ipsum has been the industry's standard dummy text ever since the 1500s, unknown printer.</p>
      </div>
      <div class="feature">
        <svg viewBox="0 0 42 42"><rect x="10" y="4" width="22" height="34" rx="3" fill="none" stroke="#1f7fd1" stroke-width="4"/><circle cx="21" cy="32" r="2" fill="#1f7fd1"/></svg>
        <h3>Campaign Synchronization Across Marketing, Advertising</h3>
        <p>Lorem ipsum is simply dummy text of the printing and typesetting industry. Lorem Ipsum has been the industry's standard dummy text ever since the 1500s, unknown printer.</p>
      </div>
    </div>
  </div>
</section>

<section class="news">
  <div class="wrap">
    <h2 class="section-title">Latest <span>News &amp; Updates</span></h2>
    <div class="title-rule"></div>
    <p class="lead">We are proud to be recognized as an industry leader, setting trends in modern methods, <span class="accent">QUALITY, AND CLIENT SATISFACTION</span> our clients are treated with respect and consideration every step of the way.</p>
    <div class="cards">
      <article class="card">
        <div class="photo" role="img" aria-label="Blueprint drawings on a desk" style="background:linear-gradient(135deg,#c9d8e6,#8aa6c2)"></div>
        <div class="body"><h4>Building responsibly for Generations</h4><div class="meta">Aug 11, 2015 &nbsp;•&nbsp; 0</div><p>Our company is proud to be recognized as an industry leader, setting trends in modern methods of work.</p></div>
      </article>
      <article class="card">
        <div class="photo" role="img" aria-label="Modern house with a pool at dusk" style="background:linear-gradient(135deg,#6d7f8f,#2f3d4b)"></div>
        <div class="body"><h4>It's not in the dreaming, it's in the doing</h4><div class="meta">Aug 11, 2015 &nbsp;•&nbsp; 0</div><p>Our company is proud to be recognized as an industry leader, setting trends in modern methods of work.</p></div>
      </article>
      <article class="card">
        <div class="photo" role="img" aria-label="Lit modern villa at night" style="background:linear-gradient(135deg,#3a3f4a,#a07a4c)"></div>
        <div class="body"><h4>Let's go invest tomorrow</h4><div class="meta">Aug 11, 2015 &nbsp;•&nbsp; 0</div><p>Our company is proud to be recognized as an industry leader, setting trends in modern methods of work.</p></div>
      </article>
    </div>
  </div>
</section>

<section class="clients">
  <div class="wrap">
    <h2 class="section-title">Our Satisfied <span>Clients</span></h2>
    <div class="title-rule"></div>
    <p class="lead">We have years of experience providing top notch services and remodeling services to top quality companies and residential clients throughout the world.</p>
  </div>
</section>

<section class="testimonial">
  <div class="avatar" role="img" aria-label="Client portrait"></div>
  <blockquote>"Nunc velit lacus sunt, facilisis, ipsum primis sollicitudin. Quis augue tandem aliquam, facilisis, pulvinar mattis. Vivamus sagittis lacus vel augue laoreet rutrum faucibus. Cum sociis et penatibus magnis, nascetur mus."</blockquote>
  <div class="name">Dario Venn</div>
  <div class="role">[ Manager - Corvell Groups ]</div>
</section>

<section class="contact">
  <div class="wrap">
    <h2 class="section-title">Get in Touch <span>With Us</span></h2>
    <div class="title-rule"></div>
    <p class="lead"><strong>WE ARE HAPPY</strong> to talk you through any projects if you are interested in our services please contact us to discuss the opportunity.</p>
    <div class="contact-grid">
      <div>
        <h3>Give us a Call</h3>
        <ul class="info-list">
          <li><i></i>Suite 210, 48 Marlow Crescent, Ashford</li>
          <li><i></i>support@brightvantage.com</li>
          <li><i></i>+(555) 014-7731</li>
          <li><i></i>www.brightvantage.com</li>
        </ul>
      </div>
      <div>
        <h3>Drop us a Message</h3>
        <div class="field">Name</div>
        <div class="field">Email</div>
        <div class="field message">Message</div>
        <span class="submit">Submit</span>
      </div>
    </div>
  </div>
</section>

<div class="map" role="img" aria-label="Street map of the office location"></div>

<footer class="site-footer">
  <div class="social"><i></i><i></i><i></i><i></i><i></i><i></i><i></i><i></i></div>
  <p>All Rights Reserved 2015</p>
</footer>

</body>
</html>
```